"Oral Surgery Office needs a Business Card Design with Logo"

We need a logo design and business card. The name of the office is Halvering Oral Surgery & Implant Center. The final design should communicate uniqueness as well as highly class office. The business card should emphasize power. I included the current business card below. Please design something unique

Target Market(s)

Dentists & Patients

Industry/Entity Type

Dental

Contact Information for Business Card

Unique Design to show success, prestige, Style, unmatched performance

Font styles to use
Serif

Colors
1b1b1b
ffffff
0556a4

Requirements
Must have
• Bussiness Name, Doctor's Name, Website, phone and Fax, email, office address
• Color should be either Black and White or Blue and White
Nice to have
• Clean look
Should not have
• the business card shouldn't be too busy. I feel like the old business card was too busy

```html
<!DOCTYPE html>
<html lang="en">
<head>
<meta charset="utf-8">
<title>Halvering Oral Surgery &amp; Implant Center – Business Card</title>
<link rel="stylesheet" href="https://fonts.googleapis.com/css2?family=Montserrat:wght@600&family=Roboto:wght@400;700&family=Roboto+Condensed:wght@400&display=swap">
<style>
  :root {
    --blue: #1f63a3;
    --ink: #1b1b1b;
    --white: #ffffff;
    --ring: #c9cbce;
    --backdrop: #e6e7e9;
  }
  * { box-sizing: border-box; margin: 0; padding: 0; }
  html, body { width: 1200px; height: 1200px; overflow: hidden; background: var(--backdrop); }
  .card {
    position: absolute; left: 239px; width: 722px; height: 441px;
    background: var(--white); overflow: hidden;
    box-shadow: 0 10px 24px rgba(0,0,0,.18);
  }
  .card--front { top: 102px; }
  .card--back { top: 625px; }

  .wordmark {
    position: absolute; top: 60px; left: 0; width: 100%;
    text-align: center; color: var(--blue);
    font-family: "Montserrat", sans-serif; font-weight: 600;
    font-size: 38px; line-height: 48px; letter-spacing: -0.5px;
  }
  .front-rule { position: absolute; top: 277px; left: 0; width: 100%; height: 11px; background: var(--ink); }
  .front-band { position: absolute; top: 288px; left: 0; width: 100%; height: 153px; background: var(--blue); color: var(--white); text-align: center; font-family: "Roboto", sans-serif; }
  .doctor-name { margin-top: 33px; font-size: 30px; font-weight: 700; letter-spacing: .3px; }
  .doctor-title { margin-top: 4px; font-size: 19px; font-weight: 400; }

  .emblem {
    position: absolute; left: 255px; top: 42px; width: 214px; height: 214px;
    border: 3px solid var(--ring); border-radius: 50%;
    display: flex; align-items: center; justify-content: center; text-align: center;
    color: var(--blue); font-family: "Montserrat", sans-serif; font-weight: 600;
    font-size: 17px; line-height: 22px; padding: 0 28px;
  }
  .contact-row {
    position: absolute; left: 0; width: 100%; background: var(--blue);
    color: var(--white); font-family: "Roboto Condensed", sans-serif; font-size: 17px;
  }
  .contact-row--1 { top: 278px; height: 46px; }
  .contact-row--2 { top: 327px; height: 46px; }
  .contact-row--3 { top: 376px; height: 65px; }
  .contact-item { position: absolute; top: 3px; display: flex; align-items: center; gap: 12px; height: 40px; white-space: nowrap; }
  .icon-badge {
    width: 40px; height: 40px; border-radius: 50%; background: var(--ink);
    display: flex; align-items: center; justify-content: center; flex: none;
  }
  .icon-badge svg { width: 22px; height: 22px; }
  .col-1 { left: 34px; } .col-2 { left: 360px; } .col-3 { left: 541px; }
</style>
</head>
<body>

<section class="card card--front">
  <h1 class="wordmark">Halvering<br>Oral Surgery &amp;<br>Implant Center</h1>
  <div class="front-rule"></div>
  <div class="front-band">
    <p class="doctor-name">Dr. Marcus Elvane, D.D.S.</p>
    <p class="doctor-title">Oral &amp; Maxillofacial Surgery</p>
  </div>
</section>

<section class="card card--back">
  <div class="emblem">Halvering Oral Surgery &amp; Implant Center</div>

  <div class="contact-row contact-row--1">
    <div class="contact-item col-1">
      <span class="icon-badge"><svg viewBox="0 0 24 24"><path d="M12 3 2 12h3v9h5v-6h4v6h5v-9h3z" fill="#fff"/></svg></span>
      <span>2048 Harbor Lane, Halvering, NY 10990</span>
    </div>
    <div class="contact-item col-2">
      <span class="icon-badge"><svg viewBox="0 0 24 24"><path d="M3 9c0-3 4-4 9-4s9 1 9 4v2h-5V9H8v2H3z" fill="#fff"/><rect x="6" y="12" width="12" height="7" rx="1" fill="#fff"/></svg></span>
      <span>555-014-4700</span>
    </div>
    <div class="contact-item col-3">
      <span class="icon-badge"><svg viewBox="0 0 24 24" fill="none" stroke="#fff" stroke-width="1.8"><rect x="4" y="10" width="16" height="10"/><path d="M7 10V4h9l2 2v4M7 15h10"/></svg></span>
      <span>555-014-5006</span>
    </div>
  </div>

  <div class="contact-row contact-row--2">
    <div class="contact-item col-1">
      <span class="icon-badge"><svg viewBox="0 0 24 24" fill="none" stroke="#fff" stroke-width="1.8"><rect x="5" y="4" width="14" height="10"/><path d="M3 19h18l-2-4H5z"/></svg></span>
      <span>www.HalveringOralSurgery.com</span>
    </div>
    <div class="contact-item col-2">
      <span class="icon-badge"><svg viewBox="0 0 24 24" fill="none" stroke="#fff" stroke-width="1.8"><rect x="8" y="8" width="9" height="13" rx="4.5"/><path d="M12.5 8v5M12 8C11 4 7 7 4 4"/></svg></span>
      <span>HalveringOralSurgeon@mail.com</span>
    </div>
  </div>

  <div class="contact-row contact-row--3">
    <div class="contact-item col-1">
      <span class="icon-badge"></span>
      <span>HalveringOral</span>
    </div>
    <div class="contact-item col-2">
      <span class="icon-badge"></span>
      <span>Halvering Oral Surgery &amp; Implant Center</span>
    </div>
  </div>
</section>

</body>
</html>
```